Accounting Firm

We are a two partner accounting firm. our business name is BELLWOOD & TRASK. We are accountants and business consultants.

We need a stationery design for our letterhead, with compliments slip, business card and envelope.

We'd like clean, professional look. I'm 39 years old and my partner is 60+, so we'd like modern yet elegant design. Dark Navy Blue as a primary colour is preferred.

Thank you.
Updates

Hi Guys

No logo.

Thanks

Industry/Entity Type

Accounting

Requirements
Must have
• Firm name :BELLWOOD & TRASK
Business Consultants & Accountants
Address: Level 2 Units 3 & 4, 17 Merrow Crescent DALEFORD SA 5099
Box address: PO Box 418 ASHGROVE SA 5098
telp: +61 8 8555 0142
fax: +61 8 8555 0187

Martin Bellwood, CA
Lucas Trask, CPA

martin.bellwood@bellwoodtrask.example.com.au
lucas.trask@bellwoodtrask.example.com.au

Dark Navy Blue as primary colour

```html
<!DOCTYPE html>
<html lang="en">
<head>
<meta charset="utf-8">
<title>Bellwood &amp; Trask — Stationery</title>
<link href="https://fonts.googleapis.com/css2?family=Jost:wght@300;400;600&display=swap" rel="stylesheet">
<style>
  :root {
    --navy: #03048a;
    --paper: #ffffff;
    --ink-grey: #8c8c8c;
    --label: #111111;
    --frame: #bdbdbd;
    --sans: "Jost", Arial, sans-serif;
  }
  * { margin: 0; padding: 0; box-sizing: border-box; }
  html, body { width: 1200px; height: 900px; overflow: hidden; background: var(--paper); }
  .sheet { position: relative; width: 1200px; height: 900px; font-family: var(--sans); }

  .section-label { position: absolute; top: 87px; font: 600 12px/1 var(--sans); color: var(--label); }
  .section-label--card { left: 62px; }
  .section-label--slip { left: 516px; }

  .piece { position: absolute; }
  .piece--navy { background: var(--navy); }
  .piece--white { background: var(--paper); border: 1px solid var(--frame); }

  .card { left: 140px; width: 270px; height: 156px; }
  .card--front { top: 307px; }
  .card--back { top: 493px; }
  .slip { left: 516px; width: 596px; height: 281px; }
  .slip--front { top: 156px; }
  .slip--back { top: 493px; }

  .firm-name { position: absolute; font-family: var(--sans); font-weight: 400; white-space: nowrap; }
  .card--front .firm-name { left: 0; right: 0; top: 68px; text-align: center; font-size: 16px; line-height: 20px; color: var(--paper); }
  .slip--front .firm-name { left: 37px; top: 32px; font-size: 18px; line-height: 22px; color: var(--navy); }

  .contact { font-weight: 300; color: var(--ink-grey); white-space: nowrap; }
  .contact__head { font-weight: 600; color: var(--navy); }
  .dots { border-top: 2px dotted var(--navy); }

  .card--back .contact { position: absolute; left: 24px; top: 13px; font-size: 7px; line-height: 10px; }
  .card--back .contact__head { font-size: 9px; line-height: 12px; }
  .card--back .dots { width: 80px; margin: 3px 0 12px; }
  .card--back .contact p + p { margin-top: 10px; }

  .slip--front .contact { position: absolute; right: 39px; top: 21px; text-align: right; font-size: 8px; line-height: 14px; }
  .slip--front .contact__head { color: var(--ink-grey); }
  .slip--front .dots { width: 74px; margin: 3px 0 3px auto; height: 8px; }
</style>
</head>
<body>
<main class="sheet">
  <h2 class="section-label section-label--card">Business card: Front and back</h2>
  <h2 class="section-label section-label--slip">Compliment slip: Front and back</h2>

  <section class="piece piece--navy card card--front">
    <div class="firm-name">Bellwood &amp; Trask</div>
  </section>

  <section class="piece piece--white card card--back">
    <div class="contact">
      <div class="contact__head">Martin Bellwood, CA</div>
      <div class="dots"></div>
      <p>Level 2 Units 3 &amp; 4, 17 Merrow Crescent,<br>Daleford, SA 5099</p>
      <p>PO Box 418, Ashgrove<br>SA 5098</p>
      <p>T: +61 8 8555 0142<br>F: +61 8 8555 0187</p>
      <p>martin.bellwood@bellwoodtrask.example.com.au</p>
    </div>
  </section>

  <section class="piece piece--white slip slip--front">
    <div class="firm-name">Bellwood &amp; Trask</div>
    <div class="contact">
      <div class="contact__head">Address</div>
      <p>Level 2 Units 3 &amp; 4,<br>17 Merrow Crescent<br>Daleford<br>SA 5099</p>
      <div class="dots"></div>
      <div class="contact__head">Box address</div>
      <p>PO Box 418<br>Ashgrove<br>SA 5098</p>
      <div class="dots"></div>
      <p>T: +61 8 8555 0142<br>F: +61 8 8555 0187</p>
      <div class="dots"></div>
      <p>martin.bellwood@bellwoodtrask.example.com.au<br>lucas.trask@bellwoodtrask.example.com.au</p>
    </div>
  </section>

  <section class="piece piece--navy slip slip--back" aria-label="Compliment slip back"></section>
</main>
</body>
</html>
```